依頼詳細
今回は、期間限定SHOP出店に伴い告知のチラシデザインを募集します!

催事出店場所の近隣住宅に配布を考えております!
チラシを見て1人でも多くの方に足を運んでいただけるような
魅力的なデザインに出会いたいです♪

宜しくお願いします!

▼期間限定ショップ内容
期間:2022年10月21日(金)~23日(日)
場所:〒596-8417 大阪府堺市西区若松台3丁215番地
営業時間:10:00~20:00
販売商品:チーズテリーヌ
記載項目
MORIZONO AND FLAVEL 738(モリゾノ アンド フラベルナナサンハチ)
大阪府大阪市北区松葉町 2-6 B2 (ミドリテラス大阪 あおぞら広場)
TEL:06-6497-2183
HP:https://flavel-sample.jp/
Instagram:https://www.instagram.com/morizono_and_flavel738/
サイズ
A4
ページ数
両面
希望イメージ
シンプル 複雑
単色 カラフル
暗い 明るい
日常 高級
遊び心 厳粛
未来的 伝統的
女性的 男性的
希望する色
設定なし
納品ファイル
• イラストレーター形式 (.ai)
補足説明
設定なし
■ 選んだ理由

期間限定ショップ出店の内容と商品について
分かりやすくシンプルにまとまっており
伝えたい情報が分かりやすいデザインだったので
選定させていただきました。

■ 提案者全員のお礼・コメント

ご提案してくださったランサーの皆様ありがとうございました。
素敵なデザインが多く迷いました。。。
今後も期間限定ショップ出店や新しい取り組みを行う際には
デザインを募集をさせていただこうとおもっておりますので
その際にはまた宜しくお願いします!
本当にありがとうございました!

```html
<!DOCTYPE html>
<html lang="ja">
<head>
<meta charset="utf-8">
<title>MORIZONO AND FLAVEL 738 期間限定SHOP</title>
<link href="https://fonts.googleapis.com/css2?family=Zen+Maru+Gothic:wght@500;700;900&family=Montserrat:wght@600;700;800&display=swap" rel="stylesheet">
<style>
:root{
  --cream:#f8f1e4;
  --paper:#fffdf8;
  --brown:#5a3a22;
  --orange:#ee7d1e;
  --terrine-light:#f2d9a6;
  --terrine-mid:#e4b765;
  --pistachio:#b9b15a;
  --berry:#e79a93;
  --line:#b9a58c;
}
*{margin:0;padding:0;box-sizing:border-box}
html,body{width:846px;height:1200px;overflow:hidden;background:var(--cream)}
body{font-family:"Zen Maru Gothic",sans-serif;color:var(--brown)}
.flyer{position:relative;width:846px;height:1200px;background:var(--cream);overflow:hidden}
.product-photo{position:absolute;left:0;top:250px;width:846px;height:560px;
  background:linear-gradient(160deg,var(--cream) 0%,var(--terrine-light) 22%,var(--terrine-mid) 40%,var(--pistachio) 62%,var(--berry) 88%,var(--paper) 100%)}
.photo-fade{position:absolute;left:0;top:640px;width:846px;height:170px;
  background:linear-gradient(180deg,rgba(255,253,248,0) 0%,var(--paper) 100%)}
.lower-panel{position:absolute;left:0;top:810px;width:846px;height:390px;background:var(--paper)}
.lead{position:absolute;left:48px;top:44px;font-size:33px;font-weight:700;line-height:1.4;letter-spacing:.02em}
.limited{position:absolute;left:48px;top:150px;font-size:40px;font-weight:900;color:var(--orange);letter-spacing:.02em}
.open-title{position:absolute;left:40px;top:190px;font-family:"Montserrat",sans-serif;font-size:138px;font-weight:800;color:var(--orange);letter-spacing:.01em;line-height:1}
.brand-name{position:absolute;right:40px;top:40px;display:flex;align-items:center;gap:10px;font-size:16px;font-weight:700;color:var(--brown);letter-spacing:.04em}
.brand-square{width:22px;height:22px;background:var(--brown);flex:none}
.tagline{position:absolute;right:46px;top:150px;text-align:right;font-size:33px;font-weight:700;line-height:1.35}
.dates{position:absolute;left:46px;top:700px;font-family:"Montserrat",sans-serif;font-weight:800;color:var(--brown);line-height:1}
.dates .num{font-size:86px;letter-spacing:-.01em}
.dates .day{font-size:18px;font-weight:700;display:inline-block;vertical-align:bottom;margin:0 4px 12px 2px}
.dates .dash{font-size:60px}
.hours{position:absolute;left:46px;top:800px;font-family:"Montserrat",sans-serif;font-size:33px;font-weight:700}
.hours small{font-size:20px;color:var(--orange);margin-right:4px}
.venue{position:absolute;left:46px;top:846px;font-size:46px;font-weight:900;letter-spacing:.04em}
.venue-address{position:absolute;left:46px;top:915px;font-size:16px;font-weight:700}
.story{position:absolute;left:486px;top:700px;width:320px;font-size:14px;font-weight:500;line-height:1.75}
.footer{position:absolute;left:0;top:1030px;width:846px;height:170px;background:var(--paper);border-top:2px solid var(--line);
  display:flex;align-items:center;padding:0 36px;gap:22px}
.footer-mark{width:40px;height:40px;background:var(--brown);flex:none}
.footer-info{flex:1}
.footer-name{font-family:"Montserrat",sans-serif;font-size:24px;font-weight:800;letter-spacing:.02em}
.footer-kana{font-size:11px;font-weight:700;margin-top:2px}
.footer-address{font-size:12px;font-weight:500;margin-top:6px;line-height:1.5}
.footer-contact{text-align:right;font-size:13px;font-weight:700;line-height:1.7}
.footer-contact .tel{font-family:"Montserrat",sans-serif;font-size:24px;font-weight:800;display:flex;align-items:center;gap:6px;justify-content:flex-end}
.footer-contact .sns{font-size:10px;font-weight:500;display:flex;align-items:center;gap:6px;justify-content:flex-end}
.sns-dot{width:16px;height:16px;border-radius:50%;background:var(--brown);display:inline-block}
</style>
</head>
<body>
<main class="flyer">
  <div class="product-photo" role="img" aria-label="ピスタチオ、プレーン、ベリーのチーズテリーヌが斜めに並んだ写真"></div>
  <div class="photo-fade"></div>
  <div class="lower-panel"></div>

  <p class="lead">フレンチから生まれた<br>チーズケーキ専門店</p>
  <p class="limited">期間限定SHOP</p>
  <h1 class="open-title">OPEN</h1>

  <p class="brand-name"><span class="brand-square"></span>MORIZONO AND FLAVEL 738</p>
  <p class="tagline">小さな<br>チーズテリーヌから<br>大きな感動を…</p>

  <div class="dates"><span class="num">10.21</span><span class="day">FRI</span><span class="dash">–</span><span class="num">23</span><span class="day">SUN</span></div>
  <p class="hours"><small>OPEN</small>10:00<small style="margin-left:4px">/ CLOSE</small>20:00</p>
  <p class="venue">わかまつスクエア</p>
  <p class="venue-address">〒596-8417 大阪府堺市西区若松台3丁215番地</p>

  <p class="story">星付きレストランで腕を磨いたフレンチシェフが素材にこだわり抜いて仕上げたチーズテリーヌ。素材の味わいを大切にした、やさしい口どけのひと品です。ちょっと特別なひとときに、大切な方への贈り物に。この機会にぜひ会場で味わってみてください。</p>

  <footer class="footer">
    <div class="footer-mark"></div>
    <div class="footer-info">
      <p class="footer-name">MORIZONO AND FLAVEL 738</p>
      <p class="footer-kana">モリゾノ アンド フラベルナナサンハチ</p>
      <p class="footer-address">大阪府大阪市北区松葉町 2-6 B2<br>ミドリテラス大阪 あおぞら広場</p>
    </div>
    <div class="footer-contact">
      <p class="tel"><svg width="20" height="20" viewBox="0 0 24 24" aria-hidden="true"><path fill="#5a3a22" d="M6.6 10.8a15.1 15.1 0 0 0 6.6 6.6l2.2-2.2a1 1 0 0 1 1-.25 11.4 11.4 0 0 0 3.6.57 1 1 0 0 1 1 1V20a1 1 0 0 1-1 1A17 17 0 0 1 3 4a1 1 0 0 1 1-1h3.5a1 1 0 0 1 1 1c0 1.25.2 2.45.57 3.57a1 1 0 0 1-.25 1z"/></svg>06-6497-2183</p>
      <p>https://flavel-sample.jp/</p>
      <p class="sns"><span class="sns-dot"></span>https://www.instagram.com/morizono_and_flavel738/</p>
    </div>
  </footer>
</main>
</body>
</html>
```